Social Media Graphics - Bright Ridge Run REVISED

Create 6-7 individual social media graphics (square size) to encourage folks to join our online course called:

The Copper Ladder Plan
How to Launch a Multi-Million Business From Scratch
Sign Up Today!

IMPORTANT: Make the largest and most prominent text on the graphic be: How to Launch a Multi-Million Business From Scratch

For the color scheme of the graphics, let's try a blue color palette; make sure the graphics appeal to both men and women

Make sure each graphic contains 1 of the 3 pics attached (crop pic as needed); and make sure one of the graphics is all TEXT only.

Target Market(s)

men and women looking to start a business

Industry/Entity Type

Entrepreneurship

Colors
0054AA
0677BA
7BADD7
CADEEF
E8F1F8

Requirements
Must have
• All the text and use the 3 pics provided; one graphic can be all text; Simple, modern design that's easy to read

```html
<!DOCTYPE html>
<html lang="en">
<head>
<meta charset="utf-8">
<title>The Copper Ladder Plan – How to Launch a Multi-Million Business From Scratch</title>
<link href="https://fonts.googleapis.com/css2?family=Archivo+Black&family=Bebas+Neue&display=swap" rel="stylesheet">
<style>
  :root {
    --navy: #03203f;
    --ink: #021a33;
    --white: #ffffff;
    --blue-strong: #0054AA;
    --blue-mid: #0677BA;
    --blue-soft: #7BADD7;
    --blue-pale: #CADEEF;
    --blue-mist: #E8F1F8;
  }
  html, body {
    margin: 0;
    padding: 0;
    width: 1200px;
    height: 1200px;
    overflow: hidden;
    background: var(--navy);
  }
  .canvas {
    position: relative;
    width: 1200px;
    height: 1200px;
    overflow: hidden;
    background: var(--navy);
  }
  .hosts-photo {
    position: absolute;
    left: 660px;
    top: 400px;
    width: 540px;
    height: 800px;
    background:
      linear-gradient(180deg, var(--navy) 0%, rgba(3,32,63,0) 20%),
      linear-gradient(90deg, var(--navy) 0%, #0b3d72 18%, var(--blue-mid) 42%, #2c5f8f 62%, #0d2c4f 85%, var(--ink) 100%);
  }
  .banner {
    position: absolute;
    left: 0;
    top: 0;
    width: 1200px;
    height: 1200px;
  }
  .banner-title {
    font-family: "Archivo Black", "Arial Black", sans-serif;
    font-size: 84px;
    fill: var(--ink);
  }
  .headline {
    position: absolute;
    left: 98px;
    top: 690px;
    margin: 0;
    font-family: "Bebas Neue", "Oswald", sans-serif;
    font-weight: 400;
    font-size: 108px;
    line-height: 96px;
    color: var(--white);
    letter-spacing: 0.5px;
  }
  .signup-button {
    position: absolute;
    left: 100px;
    top: 1086px;
    width: 316px;
    height: 76px;
    border-radius: 12px;
    background: linear-gradient(90deg, var(--blue-mist) 0%, var(--blue-pale) 50%, var(--blue-soft) 100%);
    box-shadow: 6px 7px 0 var(--blue-strong);
    display: flex;
    align-items: center;
    justify-content: center;
    font-family: "Bebas Neue", "Oswald", sans-serif;
    font-size: 56px;
    color: var(--ink);
    line-height: 1;
    padding-top: 4px;
    box-sizing: border-box;
  }
</style>
</head>
<body>
  <main class="canvas">
    <div class="hosts-photo" role="img" aria-label="Photo of the two course hosts smiling, a woman with arms crossed and a man in a dark jacket"></div>

    <svg class="banner" viewBox="0 0 1200 1200">
      <defs>
        <linearGradient id="bandFill" x1="0" y1="0" x2="1" y2="0">
          <stop offset="0" stop-color="var(--blue-mist)"/>
          <stop offset="0.45" stop-color="var(--blue-pale)"/>
          <stop offset="0.75" stop-color="var(--blue-soft)"/>
          <stop offset="1" stop-color="var(--blue-pale)"/>
        </linearGradient>
      </defs>
      <polygon class="stripe-top" points="200,175 800,-72 800,-150 200,100" fill="var(--blue-strong)"/>
      <polygon class="title-band" points="0,283 1200,-210 1200,108 0,600" fill="url(#bandFill)"/>
      <polygon class="stripe-bottom" points="0,624 620,368 620,418 0,674" fill="var(--blue-mid)"/>

      <g transform="rotate(-22.3)">
        <text class="banner-title" x="60" y="385" textLength="620" lengthAdjust="spacingAndGlyphs">THE COPPER</text>
        <text class="banner-title" x="10" y="487" textLength="700" lengthAdjust="spacingAndGlyphs">LADDER PLAN</text>
      </g>

      <g class="click-icon" fill="none" stroke="var(--white)" stroke-width="6" stroke-linecap="round">
        <line x1="994" y1="160" x2="994" y2="178"/>
        <line x1="950" y1="200" x2="968" y2="200"/>
        <line x1="963" y1="170" x2="975" y2="182"/>
        <line x1="1025" y1="170" x2="1013" y2="182"/>
        <line x1="958" y1="225" x2="972" y2="218"/>
        <line x1="1030" y1="200" x2="1016" y2="200"/>
      </g>
      <polygon class="cursor" points="978,202 978,315 1004,290 1024,328 1042,318 1023,281 1058,278" fill="var(--white)" stroke="var(--ink)" stroke-width="3" stroke-linejoin="round"/>
    </svg>

    <h1 class="headline">How To Launch<br>A Multi-Million<br>Business From<br>Scratch</h1>

    <div class="signup-button">Sign Up Today!</div>
  </main>
</body>
</html>
```